Harbour Blokes - community/social/support group for men needs a flyer

We need a flyer for our community group for display in GP clinics and other community services offices. Please refer to our website for design ideas: www.harbourblokes.org.au. We need it to be clean and simple to read.

Target Market(s)

Men 18+

Font styles to use
Serif

Colors
00a990

```html
<!DOCTYPE html>
<html lang="en">
<head>
<meta charset="utf-8">
<title>Harbour Blokes – Flyer</title>
<link rel="stylesheet" href="https://fonts.googleapis.com/css2?family=EB+Garamond:wght@400&family=Montserrat:wght@500;600;700&display=swap">
<style>
  :root {
    --stage: #4a4a4a;
    --paper: #ffffff;
    --ink: #111111;
    --black: #000000;
    --white: #ffffff;
    --brand: #00a990;
    --photo-top: #7a9a5a;
    --photo-mid: #c08a78;
    --photo-low: #b24a5c;
  }
  * { box-sizing: border-box; margin: 0; padding: 0; }
  html, body {
    width: 735px; height: 1200px; overflow: hidden;
    background: var(--stage);
  }
  .flyer {
    position: absolute; left: 10px; top: 94px;
    width: 715px; height: 1012px;
    background: var(--paper);
    font-family: "EB Garamond", Georgia, serif;
    color: var(--ink);
  }
  .hero {
    position: relative; height: 479px;
    background:
      radial-gradient(ellipse at 85% 10%, #e8eadf 0%, rgba(232,234,223,0) 35%),
      linear-gradient(180deg, var(--photo-top) 0%, #a69070 38%, var(--photo-mid) 60%, var(--photo-low) 100%);
  }
  .brand-box {
    position: absolute; left: 235px; top: 0;
    width: 276px; height: 111px;
    background: var(--black);
    display: flex; align-items: center; justify-content: center; gap: 10px;
  }
  .brand-box .mark {
    width: 14px; height: 14px; background: var(--white);
  }
  .brand-box .name {
    font-family: "Montserrat", Arial, sans-serif;
    font-weight: 500; font-size: 19px; letter-spacing: 0.5px;
    color: var(--white); text-transform: uppercase;
  }
  .tagline {
    position: absolute; left: 0; right: 0; top: 405px;
    text-align: center;
    font-family: "Montserrat", Arial, sans-serif;
    font-weight: 600; font-size: 25px; letter-spacing: 0.6px;
    color: var(--white);
  }
  .content {
    position: relative; height: 437px;
  }
  .about {
    position: absolute; left: 37px; top: 26px; width: 364px;
  }
  .about h2 {
    font-family: "Montserrat", Arial, sans-serif;
    font-weight: 700; font-size: 24px; font-variant: small-caps;
    letter-spacing: 0.5px; margin-bottom: 10px; line-height: 1.1;
  }
  .about p {
    font-size: 17px; line-height: 23px; text-align: justify;
  }
  .projects {
    position: absolute; left: 446px; top: 36px; width: 250px;
  }
  .projects h3 {
    font-family: "Montserrat", Arial, sans-serif;
    font-weight: 700; font-size: 16px; font-variant: small-caps;
    line-height: 23px; letter-spacing: 0.3px;
    margin-left: 6px; margin-bottom: 16px;
  }
  .projects ul { list-style: none; }
  .projects li, .projects .more {
    font-size: 17px; line-height: 28px;
  }
  .projects li::before { content: "• "; }
  .footer {
    height: 96px; background: var(--black); color: var(--white);
    position: relative;
  }
  .footer p {
    position: absolute; top: 12px;
    font-size: 17px; line-height: 22px;
  }
  .footer .site { left: 37px; width: 370px; }
  .footer .social { left: 444px; width: 260px; }
  .footer a { color: var(--brand); text-decoration: underline; }
</style>
</head>
<body>
  <main class="flyer">
    <section class="hero" role="img" aria-label="Photo of three smiling men standing together outdoors in front of green trees">
      <div class="brand-box">
        <span class="mark"></span>
        <span class="name">Harbour Blokes</span>
      </div>
      <p class="tagline">SOCIAL. SUPPORT. MATESHIP. COMMUNITY</p>
    </section>

    <section class="content">
      <div class="about">
        <h2>About us</h2>
        <p>Harbour Blokes Inc. is a community group that supports the positive activity, engagement and inclusion of men in Port Kellan’s harbour suburbs. Our aim is to reduce the number of men who are socially disadvantaged, marginalised or isolated to become productive, active members of the local community. We do this by providing opportunities for men (18 years+) to come together in open, non-judgemental, safe spaces and participate in a range of social activities that encourage new friendships, normalise help-seeking behaviours and link with local support services.</p>
      </div>

      <div class="projects">
        <h3>We run a number of projects each year, which currently</h3>
        <ul>
          <li>Dads and kids playgroup;</li>
          <li>Games Night;</li>
          <li>Yarning Circle (men’s discussion group);</li>
          <li>GBTIQ+ social dinners;</li>
          <li>Shared Services working bee’s;</li>
          <li>Guest speakers;</li>
          <li>Annual men’s gathering</li>
        </ul>
        <p class="more">And more.</p>
      </div>
    </section>

    <footer class="footer">
      <p class="site">For a list of our current activities and to find our how you can get involved, please visit <a href="#">www.harbourblokes.org.au</a></p>
      <p class="social">Or, join our Yarnboard page for our latest updates: <a href="#">www.yarnboard.com/harbourblokesAU/</a></p>
    </footer>
  </main>
</body>
</html>
```